Clean, minimal label design needed for new skincare line.

Want clean, minimal labels for Clean (non-toxic), cosmeceutical grade Australian-made skincare products. We are going for a minimal and simple approach to our branding so want the labelling to follow suit. Please find logos attached below. Labels are white and logo is black. Font to be black, avoid colours other than white or black.

Target Market(s)

25-65+

Industry/Entity Type

Beauty

Requirements
Must have
• On the front:
- logo
- product name eg. moisturiser 1
- descriptive words eg. light
- weight eg. 30mls/1 fl oz

On the back:
- directions eg. apply one pump both AM and PM after serum application and prior to barrier protect application.
- Cruelty free icon
- Vegan icon
- Made in Australia Icon
- Open jar with 12M Icon
Nice to have
• See above
Should not have
• Avoid colours other than white or black.

```html
<!DOCTYPE html>
<html lang="en">
<head>
<meta charset="utf-8">
<title>Back Label – Directions</title>
<link href="https://fonts.googleapis.com/css2?family=Oswald:wght@400;500;600&display=swap" rel="stylesheet">
<style>
  :root {
    --label-white: #ffffff;
    --ink-black: #111111;
    --badge-grey: #e9e9e9;
  }
  html, body {
    margin: 0;
    padding: 0;
    width: 1200px;
    height: 2177px;
    overflow: hidden;
    background: var(--label-white);
  }
  .back-label {
    position: relative;
    width: 1200px;
    height: 2177px;
    background: var(--label-white);
    color: var(--ink-black);
    font-family: "Oswald", "Arial Narrow", sans-serif;
  }
  .section-heading {
    position: absolute;
    left: 80px;
    margin: 0;
    font-size: 62px;
    font-weight: 600;
    letter-spacing: 4px;
    line-height: 1;
  }
  .body-copy {
    position: absolute;
    left: 80px;
    margin: 0;
    font-size: 50px;
    font-weight: 500;
    letter-spacing: 3px;
    line-height: 98px;
    white-space: nowrap;
  }
  .heading-instructions { top: 150px; }
  .copy-instructions { top: 240px; }
  .heading-caution { top: 628px; }
  .copy-caution { top: 716px; }
  .customer-care { top: 1222px; }
  .compliance { top: 1426px; left: 88px; line-height: 74px; }

  .icon-row { position: absolute; top: 1820px; left: 0; width: 1200px; height: 340px; }
  .made-in-badge { position: absolute; left: 100px; top: 0; width: 350px; height: 320px; }
  .vegan-badge { position: absolute; left: 520px; top: 0; width: 368px; height: 328px; }
  .open-jar { position: absolute; left: 980px; top: 160px; width: 164px; height: 172px; }
</style>
</head>
<body>
<main class="back-label">
  <h2 class="section-heading heading-instructions">INSTRUCTIONS:</h2>
  <p class="body-copy copy-instructions">Apply one pump both AM and PM<br>after serum application and<br>prior to barrier protect application</p>

  <h2 class="section-heading heading-caution">CAUTION:</h2>
  <p class="body-copy copy-caution">For external use only.<br>Aviod contact with eyes.<br>Discontinue use if irritation<br>or rash appears.</p>

  <p class="body-copy customer-care">Customer Care No. XXXX</p>

  <p class="body-copy compliance">ISO - 9001:2015<br>LIC NO. 207 ISM</p>

  <div class="icon-row">
    <svg class="made-in-badge" viewBox="0 0 350 320" role="img" aria-label="Country of origin certification badge">
      <polygon points="175,0 350,320 0,320" fill="var(--ink-black)"/>
    </svg>

    <svg class="vegan-badge" viewBox="0 0 368 328" role="img" aria-label="Vegan and cruelty free certification badge">
      <rect x="0" y="0" width="368" height="328" fill="var(--badge-grey)"/>
      <circle cx="184" cy="164" r="140" fill="var(--ink-black)"/>
    </svg>

    <svg class="open-jar" viewBox="0 0 164 172" aria-label="Period after opening: 12 months">
      <path d="M18 56 L10 20 Q30 4 70 10 L80 50" fill="none" stroke="var(--ink-black)" stroke-width="6" stroke-linejoin="round"/>
      <path d="M14 62 L150 62 L140 164 L24 164 Z" fill="var(--label-white)" stroke="var(--ink-black)" stroke-width="6" stroke-linejoin="round"/>
      <rect x="36" y="96" width="92" height="48" rx="6" fill="var(--ink-black)"/>
      <text x="82" y="132" text-anchor="middle" font-family="Oswald, sans-serif" font-weight="600" font-size="38" fill="var(--label-white)">12M</text>
    </svg>
  </div>
</main>
</body>
</html>
```